New Business Card Design Project

We are looking for a talented individual to create a truly awesome/unique business card design for us. We are looking for a someone to design something that will really stand out from the crowd - we don't mind what ideas you come up with (ie embossed/flat/matte/shine etc etc) just wow us with your creativity.
Updates

Target Market(s)

Video Games Industry Professionals (all levels of seniority from QA Testers through to CEOs)

Contact Information for Business Card

Company logo (see upload)
Company name: Northbay Play Careers Ltd
Employee Name: Darren Elsby
Job title: CEO
Website: www.nbpc2go.example
Office +44 1632 960418
Mobile: +44 7700 900276
Email: darren@nbpc2go.example

Colors

Designer to choose colors to be used in the design.

Requirements
Must have
• The business card design MUST contain all the information listed in the BUSINESS CARD DETAILS box.
• You will see the colours that are relevant to us (ie company logo) in the uploaded imagery - however you do not have to use all these colours when designing the business card itself
• MUST BE DOUBLE SIDED

```html
<!DOCTYPE html>
<html lang="en">
<head>
<meta charset="utf-8">
<title>Northbay Play Careers – Business Card</title>
<link rel="stylesheet" href="https://fonts.googleapis.com/css2?family=Work+Sans:wght@400;500;700&display=swap">
<style>
  :root {
    --navy: #1c2d5e;
    --orange: #f27a1a;
    --white: #ffffff;
    --ink: #1c2d5e;
    --backdrop: #9c9c9c;
  }
  * { margin: 0; padding: 0; box-sizing: border-box; }
  html, body {
    width: 1200px; height: 930px; overflow: hidden;
    background: var(--backdrop);
    font-family: "Work Sans", Arial, sans-serif;
  }
  .card {
    position: absolute;
    width: 560px; height: 320px;
    border-radius: 22px;
    overflow: hidden;
    box-shadow: 0 6px 18px rgba(0,0,0,.25);
  }
  /* Front */
  .card-front { left: 80px; top: 80px; background: var(--navy); }
  .front-brand {
    position: absolute; left: 0; right: 0; top: 0; bottom: 0;
    display: flex; align-items: center; justify-content: center; gap: 16px;
  }
  .brand-dot {
    width: 46px; height: 46px; border-radius: 50%;
    background: var(--white);
  }
  .brand-name {
    font-weight: 700; font-size: 34px; line-height: 1.05;
    color: var(--white); letter-spacing: .2px;
  }
  /* Back */
  .card-back { left: 560px; top: 500px; background: var(--white); }
  .back-shapes { position: absolute; inset: 0; }
  .back-brand {
    position: absolute; left: 30px; top: 34px;
    display: flex; align-items: center; gap: 10px;
  }
  .back-brand .brand-dot { width: 30px; height: 30px; background: var(--navy); }
  .back-brand .brand-name { font-size: 19px; color: var(--navy); }
  .person-name {
    position: absolute; right: 82px; top: 110px;
    font-size: 24px; font-weight: 500; color: var(--orange);
    letter-spacing: .5px; text-transform: uppercase;
  }
  .divider {
    position: absolute; left: 60px; top: 146px; width: 414px; height: 1.5px;
    background: var(--orange);
  }
  .job-title {
    position: absolute; left: 482px; top: 139px;
    font-size: 13px; color: var(--ink); letter-spacing: .5px;
  }
  .contact-list { position: absolute; list-style: none; font-size: 13px; color: var(--ink); }
  .contact-list li { display: flex; align-items: center; gap: 7px; height: 21px; }
  .contact-list svg { width: 11px; height: 11px; flex: none; }
  .phones { right: 24px; top: 176px; }
  .phones li { justify-content: flex-end; }
  .online { left: 60px; top: 182px; }
</style>
</head>
<body>

<section class="card card-front" aria-label="Card front">
  <div class="front-brand">
    <span class="brand-dot"></span>
    <span class="brand-name">Northbay Play<br>Careers</span>
  </div>
</section>

<section class="card card-back" aria-label="Card back">
  <svg class="back-shapes" viewBox="0 0 560 320" preserveAspectRatio="none">
    <polygon points="0,310 374,288 386,288 380,320 0,320" fill="var(--orange)"/>
    <polygon points="400,232 560,232 560,320 392,320" fill="var(--navy)"/>
  </svg>

  <div class="back-brand">
    <span class="brand-dot"></span>
    <span class="brand-name">Northbay Play<br>Careers</span>
  </div>

  <h1 class="person-name">Darren Elsby</h1>
  <div class="divider"></div>
  <p class="job-title">CEO</p>

  <ul class="contact-list phones">
    <li>+44 1632 960418
      <svg viewBox="0 0 12 12"><path d="M2.5 1l2 2-1 1.5c.7 1.5 2 2.8 3.5 3.5L8.5 7l2 2-1.5 1.5C5 10 2 7 1.5 2.5z" fill="none" stroke="var(--orange)" stroke-width="1.2"/></svg>
    </li>
    <li>+44 7700 900276
      <svg viewBox="0 0 12 12"><rect x="3" y="1" width="6" height="10" rx="1" fill="none" stroke="var(--orange)" stroke-width="1.2"/><line x1="5" y1="9" x2="7" y2="9" stroke="var(--orange)"/></svg>
    </li>
  </ul>

  <ul class="contact-list online">
    <li>
      <svg viewBox="0 0 12 12"><rect x="1" y="2.5" width="10" height="7" fill="none" stroke="var(--orange)" stroke-width="1.2"/><path d="M1 2.5l5 4 5-4" fill="none" stroke="var(--orange)" stroke-width="1.2"/></svg>
      darren@nbpc2go.example
    </li>
    <li>
      <svg viewBox="0 0 12 12"><circle cx="6" cy="6" r="4.6" fill="none" stroke="var(--orange)" stroke-width="1.2"/><ellipse cx="6" cy="6" rx="2" ry="4.6" fill="none" stroke="var(--orange)"/><line x1="1.4" y1="6" x2="10.6" y2="6" stroke="var(--orange)"/></svg>
      www.nbpc2go.example
    </li>
  </ul>
</section>

</body>
</html>
```